Flyer-Design für Wohungsvermietung
Zielgruppe
Ich vermiete in einer Neubausiedlung 'Rosenhang Feldbrück' Wohnungen und möchte gerne für die Erstvermietung einen Flyer erstellen lassen, welchen wir in der Region aushängen bzw. abgeben können.
Aufgabenstellung
Flyer sollte über das Format A5 verfügen und auf beiden Seiten bedruckbar sein. Die Grafik sollte ansprechend für alle Altergruppen sein. Auf den Ersten Blick sollten alle wichtige Informationen ersichtlich sein. Es handelt sich um hochwertige Mietwohnungen mit einer ausgezeichneten Aussicht auf die Alpen. Die Schule befindet sich gleich anschliessend an die neue Siedlung. Ausführliche Informationen gibt es bereits auf einer Webseite: https://www.rosenhang-feldbrueck-wohnen.ch

```html
<!DOCTYPE html>
<html lang="de">
<head>
<meta charset="utf-8">
<title>Flyer Rosenhang Feldbrück</title>
<link rel="stylesheet" href="https://fonts.googleapis.com/css2?family=Arimo:wght@400;700&display=swap">
<style>
:root{
  --red:#ad2530;
  --white:#ffffff;
  --bg:#eeeeee;
  --shadow:rgba(0,0,0,.18);
}
*{box-sizing:border-box;margin:0;padding:0}
html,body{width:1200px;height:846px;overflow:hidden;background:var(--bg);font-family:"Arimo",Arial,sans-serif}
.canvas{position:relative;width:1200px;height:846px}
.page{position:absolute;top:68px;width:500px;height:708px;background:var(--white);box-shadow:0 6px 18px var(--shadow);overflow:hidden}
.page--front{left:80px}
.page--back{left:620px}

/* front */
.front-header{position:absolute;left:0;top:0;width:100%;height:162px;background:var(--red);display:flex;align-items:center;justify-content:center;text-align:center}
.front-header h1{color:var(--white);font-size:22px;line-height:1.2;font-weight:700;text-transform:uppercase;letter-spacing:.3px}
.front-photo{position:absolute;left:0;top:170px;width:100%;height:300px;background:linear-gradient(180deg,#a9c3dd 0%,#d6e0e6 22%,#7fa55a 32%,#c9cdd0 55%,#8aa865 85%,#5f8840 100%)}
.benefits{position:absolute;left:50px;top:440px;width:410px;background:var(--white);padding:18px 14px 0 14px;list-style:none}
.benefits li{color:var(--red);font-size:13.5px;line-height:1.2;margin-bottom:11px;display:flex;align-items:center;gap:7px}
.benefits strong{font-weight:700}
.tick{width:13px;height:11px;flex:none}
.welcome{position:absolute;left:44px;top:610px;color:var(--red);font-size:15.5px;font-weight:700;line-height:1.3;text-transform:uppercase}
.brand{position:absolute;left:316px;top:620px;display:flex;align-items:center;gap:8px;color:var(--red);font-size:16px;font-weight:700}
.brand-dot{width:22px;height:22px;border-radius:50%;background:#f0b92a}

/* back */
.room-photo{position:absolute}
.room-photo--kitchen{left:0;top:0;width:100%;height:172px;background:linear-gradient(90deg,#a79a8c 0%,#dcdcdc 35%,#f0f0f0 55%,#b7c7a8 80%,#d8d8d8 100%)}
.room-photo--bath{left:0;top:178px;width:198px;height:120px;background:linear-gradient(90deg,#7b6d62 0%,#d9d6d2 50%,#5b4f47 100%)}
.room-photo--living{left:204px;top:178px;width:296px;height:120px;background:linear-gradient(90deg,#6e6a66 0%,#b9c3cc 40%,#c79a64 65%,#8c8984 100%)}
.content{position:absolute;left:0;top:280px;width:100%;height:330px;background:var(--white);padding:18px 0 0 58px;color:var(--red)}
.content h2{font-size:13px;font-weight:700;text-transform:uppercase;margin-bottom:4px}
.content ul{list-style:none;font-size:12px;line-height:1.3}
.content li{padding-left:9px;position:relative;margin-bottom:3px}
.content li::before{content:"•";position:absolute;left:0;font-size:9px}
.location{width:245px}
.flat{margin-top:20px;width:370px}
.map{position:absolute;left:310px;top:290px;width:136px;height:136px;background:linear-gradient(135deg,#fdf7e4 0%,#f7efd5 60%,#e8e4dc 100%);border:1px solid #e6e0d0}
.footer{position:absolute;left:0;bottom:0;width:100%;height:98px;background:var(--red);color:var(--white);text-align:center;padding-top:22px;font-size:13px;line-height:1.35}
.footer strong{display:block;font-size:13.5px}
</style>
</head>
<body>
<div class="canvas">

  <section class="page page--front">
    <header class="front-header">
      <h1>In der Rosenhang Feldbrück<br>vermieten wir per sofort<br>3½ bis 5½ Zimmer Wohnungen.</h1>
    </header>
    <div class="front-photo" role="img" aria-label="Luftaufnahme der Neubausiedlung mit Flachdachhäusern, Wiesen und Landschaft"></div>
    <ul class="benefits">
      <li><svg class="tick" viewBox="0 0 13 11"><path d="M1 6l4 4 7-9" fill="none" stroke="#ad2530" stroke-width="2.6"/></svg><span><strong>Top Lage:</strong> 20 Autominuten bis Bern (Zentrum)</span></li>
      <li><svg class="tick" viewBox="0 0 13 11"><path d="M1 6l4 4 7-9" fill="none" stroke="#ad2530" stroke-width="2.6"/></svg><span>Wunderbare Aussicht auf <strong>Alpenpanorama</strong></span></li>
      <li><svg class="tick" viewBox="0 0 13 11"><path d="M1 6l4 4 7-9" fill="none" stroke="#ad2530" stroke-width="2.6"/></svg><span><strong>Helle, sonnige Wohnungen</strong> mit Ausrichtung gegen Süden</span></li>
      <li><svg class="tick" viewBox="0 0 13 11"><path d="M1 6l4 4 7-9" fill="none" stroke="#ad2530" stroke-width="2.6"/></svg><span>Großzügige <strong>Attikawohnungen</strong></span></li>
      <li><svg class="tick" viewBox="0 0 13 11"><path d="M1 6l4 4 7-9" fill="none" stroke="#ad2530" stroke-width="2.6"/></svg><span><strong>Gartenwohnungen</strong> mit abgeschlossenem Wohngarten</span></li>
    </ul>
    <p class="welcome">Herzlich willkommen<br>in der Rosenhang Feldbrück</p>
    <div class="brand"><span class="brand-dot"></span><span>Rosenhang Feldbrück</span></div>
  </section>

  <section class="page page--back">
    <div class="room-photo room-photo--kitchen" role="img" aria-label="Offene Küche mit Kochinsel und großen Fenstern"></div>
    <div class="room-photo room-photo--bath" role="img" aria-label="Badezimmer mit Dusche und Lavabo"></div>
    <div class="room-photo room-photo--living" role="img" aria-label="Wohnraum mit Fensterfront und Balkon"></div>
    <div class="content">
      <h2>Lage</h2>
      <ul class="location">
        <li>Eingebettet in die reizvolle Landschaft am Südhang des Hohberg liegt Feldbrück.</li>
        <li>Nahe gelegene Kindergärten und Schulen</li>
        <li>Einkaufmöglichkeiten, Apotheke, Arzt, etc. direkt im Dorfzentrum</li>
        <li>Viele Freizeitmöglichkeiten</li>
      </ul>
      <h2 class="flat">Wohnung</h2>
      <ul>
        <li>2 Gebäude zu 13 und 8 Wohnungen mit 2½ – 5½-Zimmern</li>
        <li>Große Balkone (11 m²)</li>
        <li>Fernwärmeversorgung aus zentraler Holzschnitzelheizung</li>
        <li>Eigene Waschmaschine/Tumbler in den 4½ und 5½-Zimmer-wohnungen</li>
        <li>Hindernisfrei</li>
        <li>Mit Lift von der Einstellhalle erschlossen</li>
      </ul>
    </div>
    <div class="map" role="img" aria-label="Übersichtskarte der Region mit Lage von Feldbrück"></div>
    <footer class="footer">
      <strong>Information und Verwaltung:</strong>
      hk liegenschaften ag • Lindenweg 7 • CH-3999 Talmatt<br>
      www.hk-liegenschaften.ch • info@hk-liegenschaften.ch • 031 000 47 12
    </footer>
  </section>

</div>
</body>
</html>
```